Labels for an activated Charcoal Facial Wash, Scrub and Mask

We need a new label design for a new line of Facial products. The product, falls under our Brand Dovelin and is based on Activated Charcoal. Activated Black Charcoal Facial wash (250ml), Activated Black Charcoal Mask (100gms) and Activated Black Charcoal face scrub (100gms). We would like to see designs that are modern, clean and must communicate natural products.

```html
<!DOCTYPE html>
<html lang="en">
<head>
<meta charset="utf-8">
<title>Dovelin Activated Charcoal Labels</title>
<link href="https://fonts.googleapis.com/css2?family=Arimo:wght@400;700&family=Raleway:wght@300&display=swap" rel="stylesheet">
<style>
  :root {
    --bg-light: #f2f2f2;
    --bg-dark: #bdbdbd;
    --label-white: #ffffff;
    --leaf-tone-a: #f4f4f4;
    --leaf-tone-b: #dcdcdc;
    --charcoal: #0b0b0b;
    --charcoal-soft: #262626;
    --silver-a: #8f8f8f;
    --silver-b: #f5f5f5;
    --ink-light: #e8e8e8;
    --ink-muted: #a9a9a9;
    --plastic: #1c1c1c;
  }
  * { margin: 0; padding: 0; box-sizing: border-box; }
  html, body { width: 1200px; height: 848px; overflow: hidden; }
  body {
    position: relative;
    background: radial-gradient(ellipse at 50% 15%, var(--bg-light) 0%, #dcdcdc 55%, var(--bg-dark) 100%);
    font-family: "Arimo", Arial, sans-serif;
  }
  .label { position: absolute; overflow: hidden; background: linear-gradient(180deg, var(--charcoal-soft), var(--charcoal)); }
  .label-top { position: absolute; left: 0; right: 0; top: 0; background: var(--label-white); }
  .leaf-art { position: absolute; background: radial-gradient(ellipse at 50% 50%, var(--leaf-tone-b) 0%, var(--leaf-tone-a) 60%, var(--label-white) 100%); }
  .silver-band { position: absolute; left: 0; right: 0; height: 7px; background: linear-gradient(90deg, var(--silver-a), var(--silver-b) 45%, var(--silver-a)); }
  .line { position: absolute; left: 0; right: 0; text-align: center; white-space: nowrap; line-height: 1; }
  .brand { font-family: "Raleway", sans-serif; font-weight: 300; letter-spacing: 4px; color: var(--ink-light); }
  .brand.on-white { color: #6a6a6a; }
  .activated { font-size: 7px; color: var(--ink-muted); }
  .product { font-weight: 700; color: #fff; letter-spacing: -0.5px; }
  .variant { color: #fff; }
  .claim { display: inline-block; border: 1px solid var(--ink-muted); color: var(--ink-muted); padding: 2px 4px; font-size: 6px; line-height: 1; }
  .fine { font-size: 5.5px; color: var(--ink-muted); line-height: 1.3; }

  .pump { position: absolute; left: 150px; top: 148px; }
  .tube-cap { position: absolute; left: 372px; top: 645px; width: 74px; height: 48px; background: linear-gradient(90deg, #111, #2e2e2e 50%, #111); border-radius: 0 0 5px 5px; }
  .jar-lid { position: absolute; left: 555px; top: 469px; width: 287px; height: 63px; background: linear-gradient(180deg, #f4f4f4, #d6d6d6 60%, #c4c4c4); border-bottom: 2px solid #b0b0b0; }

  .wash-label { left: 139px; top: 271px; width: 128px; height: 422px; border-radius: 0 0 6px 6px; }
  .mask-label { left: 332px; top: 242px; width: 154px; height: 403px; }
  .scrub-jar-label { left: 555px; top: 532px; width: 287px; height: 164px; }
  .scrub-lid-label { left: 861px; top: 437px; width: 178px; height: 178px; border-radius: 50%; }
</style>
</head>
<body>

<svg class="pump" width="136" height="124" viewBox="0 0 136 124" aria-hidden="true">
  <path d="M8 8 Q10 2 20 4 L112 8 Q126 9 130 22 L124 24 Q120 16 110 17 L56 16 L56 36 L44 36 L44 16 L14 14 Q8 14 8 8 Z" fill="#1f1f1f"/>
  <rect x="22" y="62" width="71" height="62" rx="3" fill="#1a1a1a"/>
  <rect x="40" y="36" width="20" height="26" fill="#262626"/>
</svg>
<div class="tube-cap" aria-hidden="true"></div>
<div class="jar-lid" aria-hidden="true"></div>

<section class="label wash-label" aria-label="Facial wash label">
  <div class="label-top" style="height:142px;">
    <div class="leaf-art" role="img" aria-label="Line-drawn leafy branch illustration" style="inset:0;"></div>
  </div>
  <div class="silver-band" style="top:142px;"></div>
  <div class="line brand" style="top:166px;font-size:16px;">DOVELIN</div>
  <div class="line activated" style="top:211px;">ACTIVATED BLACK</div>
  <div class="line product" style="top:225px;font-size:20px;">CHARCOAL</div>
  <div class="line variant" style="top:251px;font-size:12px;">Facial wash</div>
  <div class="line" style="top:313px;"><span class="claim">SMOOTH AND SUPPLE SKIN</span></div>
  <div class="line fine" style="top:373px;">FOR ALL SKIN TYPE<br>NET VOL 250ML</div>
</section>

<section class="label mask-label" aria-label="Peel-off mask label">
  <div class="label-top" style="height:167px;">
    <div class="leaf-art" role="img" aria-label="Line-drawn leafy branch illustration" style="inset:0;"></div>
  </div>
  <div class="silver-band" style="top:167px;"></div>
  <div class="line brand" style="top:192px;font-size:16px;">DOVELIN</div>
  <div class="line activated" style="top:238px;">ACTIVATED BLACK</div>
  <div class="line product" style="top:252px;font-size:21px;">CHARCOAL</div>
  <div class="line variant" style="top:281px;font-size:9px;">Mask</div>
  <div class="line" style="top:316px;"><span class="claim">PURIFYING PEEL-OFF MASK</span></div>
  <div class="line fine" style="top:360px;">FOR ALL SKIN TYPE<br>NET VOL 100G</div>
</section>

<section class="label scrub-jar-label" aria-label="Face scrub jar label">
  <div class="label-top" style="height:80px;">
    <div class="leaf-art" role="img" aria-label="Line-drawn leaf sprig illustration" style="left:0;top:0;width:95px;height:80px;"></div>
    <div class="leaf-art" role="img" aria-label="Line-drawn leaf sprig illustration" style="right:0;top:10px;width:95px;height:70px;"></div>
  </div>
  <div class="silver-band" style="top:80px;height:5px;"></div>
  <div class="line brand on-white" style="top:36px;font-size:13px;">DOVELIN</div>
  <div class="line activated" style="top:95px;font-size:5.5px;">ACTIVATED BLACK</div>
  <div class="line product" style="top:103px;font-size:17px;">CHARCOAL</div>
  <div class="line variant" style="top:123px;font-size:6.5px;">FACE SCRUB</div>
  <div class="line" style="top:136px;"><span class="claim" style="font-size:4.5px;">DEEP CLEANSING, EXFOLIATION</span></div>
  <div class="line fine" style="top:152px;font-size:4.5px;">NET VOL 100G</div>
</section>

<section class="label scrub-lid-label" aria-label="Face scrub lid label">
  <div class="label-top" style="height:104px;">
    <div class="leaf-art" role="img" aria-label="Line-drawn leaf sprigs around the rim" style="inset:0;"></div>
  </div>
  <div class="silver-band" style="top:104px;height:5px;"></div>
  <div class="line brand on-white" style="top:63px;font-size:12px;">DOVELIN</div>
  <div class="line activated" style="top:124px;font-size:6.5px;">ACTIVATED BLACK</div>
  <div class="line product" style="top:135px;font-size:20px;">CHARCOAL</div>
  <div class="line variant" style="top:159px;font-size:8px;letter-spacing:0.3px;">FACE SCRUB</div>
  <div class="line" style="top:170px;"><span class="claim" style="font-size:4.5px;">DEEP CLEANSING, EXFOLIATION</span></div>
</section>
<div class="line fine" style="left:861px;width:178px;top:659px;font-size:4.5px;">NET VOL 100G</div>

</body>
</html>
```